Refresh of a rather uncommon tech outfit website

Our web site is starting to show it's age. You can see the existing site here: www.plumfarrow.net. As a growing company we want to come across as a dynamic collection of IT experts.

We want to update the design so are open to any colour palette and look, but want to retain our current table logo. We use the logo on our business cards but with a white background - see the attached file, so you don't need to keep the brown or the green.

The design should consider the range of browsers that will be looking at the site - so please show how it will look on a wide screen laptop and a 768x1024 tablet.

We want to add some pages about our team and their skills, probably with photos of each person on the team.

This is an uncoded project - the PSD files of the design is required, not coding.
Updates

Thanks everyone for the submissions so far.  It's a holiday day in the UK today but we will get some feedback on the designs so far out to you.

Target Market(s)

Architects and other creative types looking for IT support

Industry/Entity Type

Business

Font styles to use
Serif
Sans Serif

Requirements
Must have
• Must look good on a laptop and an Zelva.

```html
<!DOCTYPE html>
<html lang="en">
<head>
<meta charset="utf-8">
<title>plumfarrow.net — a rather uncommon tech outfit</title>
<link rel="stylesheet" href="https://fonts.googleapis.com/css2?family=Open+Sans:ital,wght@0,300;0,400;0,600;1,300;1,400&display=swap">
<style>
  :root {
    --page-bg: #ffffff;
    --header-top: #ffffff;
    --header-bottom: #d6d7d9;
    --band: #c8870b;
    --band-dark: #a86f06;
    --logo-mark: #e2b000;
    --ink: #333333;
    --ink-soft: #666666;
    --nav-top: #ffffff;
    --nav-bottom: #e6e6e6;
    --white: #ffffff;
    --card-line: #dddddd;
    --hero-a: #dfe4e8;
    --hero-b: #9aa5ad;
    --hero-c: #4a5560;
  }
  * { box-sizing: border-box; margin: 0; padding: 0; }
  html, body {
    width: 1200px; height: 725px; overflow: hidden;
    background: var(--page-bg);
    font-family: "Open Sans", Arial, sans-serif;
    color: var(--ink);
  }
  .site { position: relative; width: 1200px; height: 725px; overflow: hidden; }
  .site-header {
    position: absolute; left: 0; top: 0; width: 1200px; height: 250px;
    background: linear-gradient(to bottom, var(--header-top) 0%, var(--header-top) 35%, var(--header-bottom) 100%);
  }
  .content-band {
    position: absolute; left: 0; top: 250px; width: 1200px; height: 475px;
    background: var(--band);
  }
  .container { position: absolute; left: 170px; width: 860px; }

  .brand { top: 34px; display: flex; align-items: center; gap: 10px; }
  .brand-mark { width: 22px; height: 22px; background: var(--logo-mark); }
  .brand-name { font-size: 24px; font-weight: 600; color: var(--ink); letter-spacing: -0.3px; }

  .main-nav {
    top: 96px; height: 40px;
    background: linear-gradient(to bottom, var(--nav-top), var(--nav-bottom));
    border-radius: 4px 4px 0 0;
    box-shadow: 0 2px 6px rgba(0,0,0,0.12);
    display: flex; align-items: center; padding-left: 18px; gap: 20px;
  }
  .main-nav a { font-size: 14px; color: var(--ink); text-decoration: none; }

  .hero {
    top: 136px; height: 268px;
    background:
      radial-gradient(ellipse at 30% 40%, rgba(255,255,255,0.35), transparent 55%),
      linear-gradient(120deg, var(--hero-a) 0%, var(--hero-b) 55%, var(--hero-c) 100%);
    box-shadow: 0 6px 14px rgba(0,0,0,0.25);
  }
  .slider-control {
    position: absolute; left: 380px; bottom: -12px; width: 104px; height: 26px;
    background: linear-gradient(to bottom, #ffffff, #dcdcdc);
    border-radius: 5px; box-shadow: 0 1px 4px rgba(0,0,0,0.3);
  }

  .tagline {
    top: 420px; text-align: center;
    font-size: 26px; font-weight: 300; font-style: italic; line-height: 34px;
    color: var(--white);
  }

  .columns { top: 510px; height: 195px; display: flex; gap: 40px; }
  .column { width: 250px; color: var(--white); position: relative; }
  .column h2 { font-size: 15px; font-weight: 400; margin-bottom: 10px; }
  .column p { font-size: 11px; line-height: 16px; color: #fbeed3; }
  .button {
    display: inline-block; margin-top: 14px;
    background: var(--white); color: var(--ink);
    font-size: 10px; padding: 5px 12px; border-radius: 3px;
  }
  .blog-card {
    width: 280px; background: var(--white); border-radius: 4px;
    padding: 10px 14px; box-shadow: 0 2px 6px rgba(0,0,0,0.25);
  }
  .blog-card h2 { font-size: 15px; font-weight: 400; color: var(--ink); padding-bottom: 6px; border-bottom: 1px solid var(--card-line); }
  .blog-list { list-style: none; }
  .blog-list li { display: flex; gap: 8px; padding: 7px 0; border-bottom: 1px solid var(--card-line); }
  .blog-list li:last-child { border-bottom: none; }
  .blog-title { font-size: 11px; color: var(--ink); }
  .blog-meta { font-size: 9px; color: var(--ink-soft); }
</style>
</head>
<body>
<div class="site">
  <header class="site-header"></header>
  <div class="content-band"></div>

  <div class="container brand">
    <span class="brand-mark"></span>
    <span class="brand-name">plumfarrow.net</span>
  </div>

  <nav class="container main-nav">
    <a href="#">Home</a><a href="#">About</a><a href="#">Strategy</a><a href="#">Digital</a><a href="#">Technology</a><a href="#">Operations</a><a href="#">Industries</a>
  </nav>

  <div class="container hero" role="img" aria-label="Photo of two colleagues in business attire reviewing data on a phone in a bright office">
    <div class="slider-control">
      <svg width="104" height="26" viewBox="0 0 104 26">
        <polyline points="14,7 9,13 14,19" fill="none" stroke="#777" stroke-width="2"/>
        <circle cx="32" cy="13" r="5" fill="#cfcfcf"/>
        <circle cx="45" cy="13" r="5" fill="#cfcfcf"/>
        <circle cx="58" cy="13" r="5" fill="#c8870b"/>
        <circle cx="71" cy="13" r="5" fill="#cfcfcf"/>
        <polyline points="89,7 94,13 89,19" fill="none" stroke="#777" stroke-width="2"/>
      </svg>
    </div>
  </div>

  <p class="container tagline">“Without big data analytics, companies are blind and deaf,<br>wandering out onto the Web like deer on a freeway.”</p>

  <section class="container columns">
    <div class="column">
      <h2>Who We Are</h2>
      <p>We are a small team of engineers, designers and support staff who keep studios running smoothly, from networks and servers to the software creative people rely on every day.</p>
      <span class="button">Learn More</span>
    </div>
    <div class="column">
      <h2>What We Do</h2>
      <p>We plan, build and look after IT for architects and creative firms, covering hardware, cloud storage, backups, security and help desk support that answers quickly.</p>
      <span class="button">Learn More</span>
    </div>
    <aside class="blog-card">
      <h2>From The Blog</h2>
      <ul class="blog-list">
        <li><svg width="8" height="20" viewBox="0 0 8 20"><polyline points="2,5 6,9 2,13" fill="none" stroke="#999" stroke-width="1.5"/></svg><div><div class="blog-title">New render farm setup</div><div class="blog-meta">Posted by admin on May 12</div></div></li>
        <li><svg width="8" height="20" viewBox="0 0 8 20"><polyline points="2,5 6,9 2,13" fill="none" stroke="#999" stroke-width="1.5"/></svg><div><div class="blog-title">Backups that actually work</div><div class="blog-meta">Posted by admin on May 08</div></div></li>
        <li><svg width="8" height="20" viewBox="0 0 8 20"><polyline points="2,5 6,9 2,13" fill="none" stroke="#999" stroke-width="1.5"/></svg><div><div class="blog-title">Choosing a studio NAS</div><div class="blog-meta">Posted by admin on Apr 29</div></div></li>
        <li><svg width="8" height="20" viewBox="0 0 8 20"><polyline points="2,5 6,9 2,13" fill="none" stroke="#999" stroke-width="1.5"/></svg><div><div class="blog-title">Faster Wi-Fi for studios</div><div class="blog-meta">Posted by admin on Apr 21</div></div></li>
      </ul>
    </aside>
  </section>
</div>
</body>
</html>
```